Parades of Glint stationary design

Parades of Glint (www.paradesofglint.example) is a company that operates events that display the worlds most exotic cars, motorcyles, aircraft, watercraft and luxury brands. we are cutting edge and are looking for a clean , modern stationary design. our sponsors of the events include names like Vantorro, Molvecci, Castelvandri, Kelmayr, Ravelli, Lun vorel, Quastmere and many other big names. we currently operate in florida but are looking to get into new York and California. I added the logo and two car images.car images are optional and not mandatory for the design. Just thought we would add to see what happens.

Target Market(s)

high end , clean design think KELMAYR DESGN style sharp, clean, cutting edge must appeal to the high end luxury brand corporate companies and car, motorcycle, boat, aircraft and luxury brand collectors

Industry/Entity Type

Events

Font styles to use
Sans Serif

Requirements
Must have
• our contact information
• Neil Horvath
• President
• 352-555-0174
• www.paradesofglint.example
• PO Box 4862
• Dunmore, FL 32000
• for business card my email is neil@paradesofglint.example

```html
<!DOCTYPE html>
<html lang="en">
<head>
<meta charset="utf-8">
<title>Parades of Glint – Stationery</title>
<link rel="stylesheet" href="https://fonts.googleapis.com/css2?family=Tinos:wght@400;700&family=Arimo:wght@400&display=swap">
<style>
  :root {
    --backdrop: #98436f;
    --paper: #ffffff;
    --ink-dark: #3a3a3a;
    --ink-maroon: #7a1a2a;
    --rule-grey: #8a8a8a;
    --watermark: #c9c9c9;
    --chrome-dark: #7d7d7d;
    --chrome-light: #f4f4f4;
    --maroon-band: #6e1424;
    --car-red: #7a2030;
    --car-shadow: #2b2b2b;
  }
  * { margin: 0; padding: 0; box-sizing: border-box; }
  html, body { width: 1200px; height: 800px; overflow: hidden; }
  body {
    background: var(--backdrop);
    position: relative;
    font-family: "Tinos", "Times New Roman", serif;
    color: var(--ink-maroon);
  }
  .sheet {
    position: absolute;
    background: var(--paper);
    overflow: hidden;
  }
  .brand-name {
    position: absolute;
    font-family: "Tinos", "Times New Roman", serif;
    font-weight: 700;
    color: var(--ink-dark);
    text-transform: uppercase;
    white-space: nowrap;
    letter-spacing: 0.5px;
  }
  .car-visual {
    position: absolute;
    top: 0;
    right: 0;
    background:
      radial-gradient(ellipse 55% 35% at 48% 62%, var(--car-red) 0%, rgba(122,32,48,0.85) 45%, rgba(255,255,255,0) 75%),
      linear-gradient(250deg, var(--car-shadow) 0%, #9a9a9a 35%, rgba(255,255,255,0) 70%);
  }
  .chrome-band {
    position: absolute;
    left: 0;
    right: 0;
    bottom: 0;
    background: linear-gradient(to bottom,
      var(--chrome-dark) 0%, var(--chrome-light) 30%, #d8d8d8 50%,
      var(--chrome-light) 65%, var(--chrome-dark) 100%);
  }
  .chrome-band::after {
    content: "";
    position: absolute;
    left: 0; right: 0; bottom: 0;
    background: linear-gradient(to bottom, #9c4858, var(--maroon-band));
  }

  /* Letterhead */
  .letterhead { left: 47px; top: 87px; width: 427px; height: 604px; }
  .letterhead .brand-name { left: 38px; top: 18px; font-size: 22px; }
  .letterhead .car-visual { width: 190px; height: 88px; }
  .letterhead .contact {
    position: absolute;
    right: 4px;
    top: 91px;
    text-align: right;
    font-size: 10px;
    line-height: 12px;
    color: var(--ink-maroon);
  }
  .letterhead .holder-name {
    position: absolute;
    left: 9px;
    top: 104px;
    font-family: "Arimo", Arial, sans-serif;
    font-size: 19px;
    color: var(--ink-maroon);
  }
  .letterhead .header-rule {
    position: absolute;
    left: 0; right: 0;
    top: 124px;
    height: 1px;
    background: var(--rule-grey);
  }
  .letterhead .watermark-name {
    position: absolute;
    left: 0; right: 0;
    top: 262px;
    text-align: center;
    font-weight: 700;
    font-size: 36px;
    color: var(--watermark);
    text-transform: uppercase;
    letter-spacing: 1px;
  }
  .letterhead .chrome-band { height: 42px; }
  .letterhead .chrome-band::after { height: 12px; }

  /* Business card, large */
  .card-front { left: 569px; top: 144px; width: 471px; height: 237px; }
  .card-front .brand-name { left: 22px; top: 14px; font-size: 25px; }
  .card-front .car-visual { width: 215px; height: 178px; }
  .card-front .role { position: absolute; left: 44px; top: 119px; font-size: 11px; color: var(--ink-dark); }
  .card-front .holder-name { position: absolute; left: 27px; top: 133px; font-size: 15px; }
  .card-front .contact {
    position: absolute; left: 27px; top: 153px;
    font-size: 9px; line-height: 11px;
  }
  .card-front .chrome-band { height: 48px; }
  .card-front .chrome-band::after { height: 14px; }

  /* Business card, small */
  .card-detail { left: 520px; top: 433px; width: 424px; height: 234px; }
  .card-detail .brand-name { left: 52px; top: 10px; font-size: 20px; }
  .card-detail .car-visual { width: 217px; height: 115px; }
  .card-detail .contact-block {
    position: absolute; left: 16px; top: 92px;
    font-size: 14px; line-height: 16.5px;
  }
  .card-detail .contact-block .role { font-size: 11.5px; color: var(--ink-dark); }
  .card-detail .chrome-band { height: 44px; }
  .card-detail .chrome-band::after { height: 13px; }
</style>
</head>
<body>

<section class="sheet letterhead" aria-label="Letterhead">
  <div class="brand-name">Parades of Glint</div>
  <div class="car-visual" role="img" aria-label="Photograph of a dark red vintage sports car"></div>
  <div class="contact">
    <div>Tel: 352-555-0174</div>
    <div>web: www.paradesofglint.example</div>
    <div>PO Box 4862, Dunmore, FL 32000</div>
  </div>
  <div class="holder-name">Neil Horvath</div>
  <div class="header-rule"></div>
  <div class="watermark-name">Parades of Glint</div>
  <div class="chrome-band"></div>
</section>

<section class="sheet card-front" aria-label="Business card">
  <div class="brand-name">Parades of Glint</div>
  <div class="car-visual" role="img" aria-label="Photograph of a dark red vintage sports car"></div>
  <div class="role">President</div>
  <div class="holder-name">Neil Horvath</div>
  <div class="contact">
    <div>Tel: 352-555-0174</div>
    <div>web: www.paradesofglint.example</div>
    <div>PO Box 4862, Dunmore, FL 32000.</div>
  </div>
  <div class="chrome-band"></div>
</section>

<section class="sheet card-detail" aria-label="Business card with email">
  <div class="brand-name">Parades of Glint</div>
  <div class="car-visual" role="img" aria-label="Photograph of a dark red vintage sports car"></div>
  <div class="contact-block">
    <div class="role">President</div>
    <div>Neil Horvath</div>
    <div>Tel: 352-555-0174</div>
    <div>E-Mail: neil@paradesofglint.example</div>
    <div>web: www.paradesofglint.example</div>
    <div>PO Box 4862, Dunmore, FL 32000.</div>
  </div>
  <div class="chrome-band"></div>
</section>

</body>
</html>
```